Redesign our website!

Tandlo’ current web (http://tandlo-example.com) site was implemented in 2012 and needs to be brought up to date with look and feel of our new packaging and logo. The layout of Tandlo’ website is fairly consistent from page to page; utilizing only two very similar “templates” or “themes.”

Tandlo is seeking a designer to gain inspiration from our new packaging, design and recent print ad and create a new look for our website (http://tandlo-example.com); focusing on the wallpaper, background, navigation bars/buttons, header and footer. Additionally, Tandlo needs a new “style” for the images used in the slideshow on the homepage as well as the banner images on the product category/subcategory pages.

It is important that element height/width and positioning of elements (such as the "feature" boxes on the homepage, navigation bar, and banner images) within the pages are not changed in the new design. In other words, this project is solely focused on the overall design, not the specific layouts of each page.

Attached are:
* a zip file of JPEG examples of our new packaging;
* a pdf copy of a print ad we recently used for an industry tradeshow;
* a zip file with 2 JPEGS of images used in our booth at the above mentioned tradeshow;
* a JPEG of our new logo;
* a JPEG of the Background used on our new packing.

The model images that can be used in the mock-up of the new homepage slideshow but please do not feel as though you need to use the models in your banner mock-up. If you use your own models (stock images are OK,) please try to incorporate our products on the models.This will help us get a realistic sense of your direction.

I am very encouraged by the examples I am seeing. Thank you to those who have contributed and to those still working on it, please do! This is by no means a done deal with any one design.

One tip to those who have already contributed and those still to do so: we are looking for a new color scheme. Please do not use the brown/green you see on the current site.  Thank you.

• Remove "Vines" from the background"
Change the header to less look "yoga"ish
1 "sample" image for the homepage slideshow
1 "sample image" for a category banner (i.e. the banner on http://tandlo-example.com/quorvets/)

```html
<!DOCTYPE html>
<html lang="en">
<head>
<meta charset="utf-8">
<title>Tandlo – Home</title>
<link href="https://fonts.googleapis.com/css2?family=Quicksand:wght@500;700&family=Open+Sans:wght@400;600&family=Nothing+You+Could+Do&display=swap" rel="stylesheet">
<style>
:root{
  --ink:#2b2b2b;
  --header:#2f2f2f;
  --footer:#3b3b3b;
  --blue:#1aa6dc;
  --orange:#f04e1c;
  --white:#ffffff;
  --grey:#8a8a8a;
  --line:#cfcfcf;
}
*{margin:0;padding:0;box-sizing:border-box}
html,body{width:1014px;height:1200px;overflow:hidden}
body{position:relative;background:#f4f4f4;font-family:"Open Sans",sans-serif;color:var(--ink)}
.abs{position:absolute}
a{color:inherit;text-decoration:none}

/* header */
.site-header{left:0;top:0;width:1014px;height:78px;background:radial-gradient(ellipse at 50% 40%,#3c3c3c,#262626)}
.brand{left:158px;top:10px;font-family:"Quicksand",sans-serif;font-weight:500;font-size:42px;color:var(--white);letter-spacing:-1px}
.top-links{right:158px;top:14px;font-size:10px;color:var(--white)}
.top-links span{margin:0 4px}
.social-top{left:641px;top:40px;display:flex;gap:7px}
.social-top i{width:19px;height:19px;border-radius:50%;background:var(--white);display:block}
.search{left:746px;top:41px;width:110px;height:18px;background:var(--white);border-radius:2px;font-size:10px;color:#999;padding:2px 6px}

/* nav */
.main-nav{left:0;top:78px;width:1014px;height:32px;background:var(--blue);border-top:1px dashed rgba(255,255,255,.6);border-bottom:1px dashed rgba(255,255,255,.6)}
.main-nav a{position:absolute;top:0;height:30px;line-height:30px;text-align:center;font-family:"Quicksand",sans-serif;font-weight:700;font-size:12.5px;color:var(--white);border-right:1px solid rgba(255,255,255,.3)}
.main-nav a.active{background:var(--orange)}

/* hero */
.hero{left:0;top:110px;width:1014px;height:384px;background:linear-gradient(180deg,#e9ebe9 0%,#c9b79a 22%,#8c8a7a 34%,#8d97a1 48%,#6d6b66 70%,#9a8f86 85%,#f4f4f4 100%)}
.hero-title{left:158px;top:186px;font-family:"Quicksand",sans-serif;font-weight:700;font-size:38px;color:#222;letter-spacing:-1px}
.hero-sub{left:158px;top:231px;font-size:26px;color:#2a2a2a;letter-spacing:.5px}
.hero-text{left:158px;top:272px;width:340px;font-size:11.5px;line-height:14px;color:#1f1f1f}
.btn-quote{left:158px;top:314px;width:226px;height:36px;background:var(--blue);color:var(--white);font-size:15px;line-height:36px;text-align:center;border-bottom:1px dashed rgba(255,255,255,.7)}
.learn{left:402px;top:325px;font-family:"Quicksand",sans-serif;font-weight:700;font-size:11px;color:var(--white)}
.slide-arrow{top:248px;width:32px;height:32px;border-radius:50%;background:rgba(200,200,200,.55)}
.tagline{left:654px;top:398px;font-family:"Nothing You Could Do",cursive;font-size:25px;color:var(--white)}

/* features */
.features{left:158px;top:444px;width:698px;height:264px;background:var(--white);box-shadow:0 0 3px rgba(0,0,0,.15)}
.sec-title{font-family:"Quicksand",sans-serif;font-weight:700;font-size:19px;color:#222}
.btn-all{left:550px;top:471px;width:96px;height:15px;background:var(--orange);color:var(--white);font-size:7.5px;line-height:15px;text-align:center}
.btn-all-tip{left:646px;top:471px}
.sec-text{font-size:11px;line-height:12px;color:var(--grey)}
.card{top:537px;width:156px;height:136px}
.card .caption{position:absolute;left:0;bottom:0;width:100%;height:29px;background:rgba(30,30,30,.85);color:var(--white);font-size:11px;line-height:29px;text-align:center}
.product-box{left:676px;top:537px;width:165px;height:137px;border:1px solid #ddd}
.pack{top:545px;width:57px;height:122px}
.mini-arrow{top:596px;width:14px;height:14px;border-radius:50%;background:var(--orange)}

/* footer */
.site-footer{left:0;top:708px;width:1014px;height:388px;background:var(--footer)}
.f-title{top:748px;font-family:"Quicksand",sans-serif;font-weight:500;font-size:16px;color:var(--white)}
.review-name{left:185px;top:778px;font-style:italic;font-size:13px;color:var(--orange)}
.review-text{left:185px;top:800px;width:150px;font-family:Georgia,serif;font-style:italic;font-size:9.3px;line-height:11.4px;color:var(--white)}
.quote-mark{font-family:Georgia,serif;font-size:26px;font-weight:700;color:var(--white)}
.info-list{top:780px;list-style:none}
.info-list li{height:22.8px;line-height:18px;font-size:9px;color:var(--white);border-bottom:1px solid #9a9a9a;padding-left:12px;position:relative}
.info-list li::before{content:"›";position:absolute;left:3px;color:#bbb}
.info-list li:last-child{border-bottom:0}
.social-circle{top:787px;width:34px;height:34px;border-radius:50%;background:var(--white)}
.contact-line{font-size:12px;color:var(--white)}
.btn-connect{left:674px;top:888px;width:181px;height:29px;background:var(--orange);color:var(--white);font-size:11.5px;line-height:29px;text-align:center;border-bottom:1px dashed rgba(255,255,255,.6)}
.gallery-title{left:0;top:949px;width:1014px;text-align:center;font-family:"Quicksand",sans-serif;font-weight:500;font-size:16px;color:var(--white)}
.thumb{top:989px;width:88px;height:61px;border:3px solid var(--white)}
.thumb-label{top:1058px;width:88px;text-align:center;font-size:10px;color:var(--white)}

/* bottom bar */
.base-bar{left:0;top:1096px;width:1014px;height:104px;background:var(--blue)}
.base-dot{left:488px;top:1069px;width:38px;height:38px;border-radius:50%;background:var(--blue)}
.copyright{left:0;top:1112px;width:1014px;text-align:center;font-size:8.5px;line-height:11px;color:var(--white)}
.base-brand{left:0;top:1138px;width:1014px;text-align:center;font-family:"Quicksand",sans-serif;font-weight:500;font-size:20px;color:var(--white)}
</style>
</head>
<body>

<header class="abs site-header"></header>
<div class="abs brand">Tandlo</div>
<nav class="abs top-links"><a>Home</a><span>/</span><a>About</a><span>/</span><a>Contact</a><span>/</span><a>Signin</a><span>/</span><a>Signup</a></nav>
<div class="abs social-top"><i></i><i></i><i></i>
  <svg width="19" height="19" viewBox="0 0 19 19"><circle cx="9.5" cy="9.5" r="9.5" fill="#fff"/><path d="M4 6h2l1.5 6h6l1.5-4.5H7" fill="none" stroke="#2f2f2f" stroke-width="1.3"/><circle cx="8" cy="14" r="1" fill="#2f2f2f"/><circle cx="13" cy="14" r="1" fill="#2f2f2f"/></svg>
</div>
<div class="abs search">Search</div>

<nav class="abs main-nav">
  <a style="left:158px;width:148px">Quorvets Brist Wallets</a>
  <a class="active" style="left:306px;width:166px">Aurloops Ear Warmers</a>
  <a style="left:472px;width:99px">Apparel</a>
  <a style="left:571px;width:115px">Accessories</a>
  <a style="left:686px;width:118px">Eco Products</a>
  <a style="left:804px;width:52px;border-right:0">Blog</a>
</nav>

<section class="abs hero" role="img" aria-label="Slideshow photo: a couple sitting in a rowboat on a lake, the woman wearing a knit cap and red hand warmers"></section>
<h1 class="abs hero-title">Welcome to Tandlo</h1>
<h2 class="abs hero-sub">QUORVETS WRIST WALLETS</h2>
<p class="abs hero-text">Lorem ipsum dolor sit amet, adipisicing elit, sed do labore sd eiusmod tempor&nbsp; labore et dolore magna adipisicing...</p>
<a class="abs btn-quote">FREE REQUEST A QUOTE</a>
<a class="abs learn">LEARN MORE</a>
<div class="abs slide-arrow" style="left:112px"><svg width="32" height="32"><path d="M18 10l-6 6 6 6" fill="none" stroke="#fff" stroke-width="3"/></svg></div>
<div class="abs slide-arrow" style="left:872px"><svg width="32" height="32"><path d="M14 10l6 6-6 6" fill="none" stroke="#fff" stroke-width="3"/></svg></div>
<div class="abs tagline">Go with the Flow</div>

<section class="abs features"></section>
<h2 class="abs sec-title" style="left:208px;top:465px">Our Features Products, H2 Heading</h2>
<a class="abs btn-all">VIEW OUR ALL FEATURS</a>
<svg class="abs btn-all-tip" width="8" height="15"><path d="M0 0h2l6 7.5-6 7.5H0z" fill="#f04e1c"/></svg>
<p class="abs sec-text" style="left:176px;top:497px;width:470px">Lorem ipsum dolor sit amet, consectetur adipisicing elit, sed do eiusmod tempor incididunt ut labore et dolore magna aliqua. Ut enim ad minim veniam, quis nostrud exercitation</p>
<h2 class="abs sec-title" style="left:708px;top:465px">Look at THAT!</h2>
<p class="abs sec-text" style="left:676px;top:497px;width:170px">Lorem ipsum dolor sit amet, sed do eiusmod tempor incididunt</p>

<div class="abs card" style="left:176px;background:linear-gradient(135deg,#b0472e,#3d8a3a 55%,#6e6a64)" role="img" aria-label="Close-up of a green leather wrist wallet on a wrist"><div class="caption">You Can Take It with You</div></div>
<div class="abs card" style="left:338px;background:linear-gradient(180deg,#c8cbc0,#8c9aa6 45%,#6b6f5a)" role="img" aria-label="Two runners by a lake wearing wrist wallets"><div class="caption">Quorvets Wrist Wallets</div></div>
<div class="abs card" style="left:500px;background:linear-gradient(135deg,#5d6a3e,#6e7048 50%,#3e3a30)" role="img" aria-label="Braided leather cuff on a forearm against an olive jacket"><div class="caption">H3 Lorem Ipsum Head</div></div>

<div class="abs product-box"></div>
<div class="abs pack" style="left:696px;background:linear-gradient(180deg,#3b3b44 75%,#2fb24a 88%)" role="img" aria-label="Product package, classic wrist wallet"></div>
<div class="abs pack" style="left:759px;background:linear-gradient(180deg,#3b3b44 75%,#1aa6dc 88%)" role="img" aria-label="Product package, two-pocket wrist wallet"></div>
<div class="abs mini-arrow" style="left:671px"><svg width="14" height="14"><path d="M8 4l-3 3 3 3" fill="none" stroke="#fff" stroke-width="1.6"/></svg></div>
<div class="abs mini-arrow" style="left:832px"><svg width="14" height="14"><path d="M6 4l3 3-3 3" fill="none" stroke="#fff" stroke-width="1.6"/></svg></div>

<footer class="abs site-footer"></footer>
<h3 class="abs f-title" style="left:158px">Client Reviews................</h3>
<div class="abs quote-mark" style="left:158px;top:772px">“</div>
<div class="abs review-name">Marla Oyen, USA</div>
<p class="abs review-text">Lorem ipsum dolor sit amet, consectetur adipisicing elit, sed do eiusmod tempor incididunt ut labore et dolore magna aliqua. Ut enim ad minim veniam, quis nostrud exercitation ullamco laboris nisi ut aliquip ex ea commodo consequat. .</p>
<div class="abs quote-mark" style="left:310px;top:890px">”</div>

<h3 class="abs f-title" style="left:401px">Tandlo Information...........................</h3>
<ul class="abs info-list" style="left:401px;width:77px"><li>Home</li><li>About</li><li>Services</li><li>Press/Media</li><li>Contact</li><li>Blog</li></ul>
<ul class="abs info-list" style="left:489px;width:110px"><li>Advocates &amp; Affiliates..</li><li>Back Story</li><li>News</li><li>Join Our Mailing List</li><li>Returns/Exchanges</li><li>FAQs</li></ul>

<h3 class="abs f-title" style="left:674px">Our Social Share................</h3>
<div class="abs social-circle" style="left:674px"></div>
<div class="abs social-circle" style="left:719px"></div>
<div class="abs social-circle" style="left:765px"></div>
<div class="abs social-circle" style="left:809px"></div>
<svg class="abs" style="left:675px;top:839px" width="10" height="12"><path d="M2 1l2 0 1 3-1.5 1c.5 1.5 1.5 2.5 3 3l1-1.5 3 1v2c-5 1-9.5-3.5-8.5-8.5z" fill="#fff"/></svg>
<div class="abs contact-line" style="left:692px;top:838px">555-014-2266 <span style="color:var(--blue)">F</span> 555-014-2267</div>
<svg class="abs" style="left:675px;top:860px" width="12" height="9"><rect x=".5" y=".5" width="11" height="8" fill="none" stroke="#fff"/><path d="M.5.5l5.5 4.5 5.5-4.5" fill="none" stroke="#fff"/></svg>
<div class="abs contact-line" style="left:692px;top:856px">sales@tandlo-example.com</div>
<a class="abs btn-connect">GET CONNECT WITH US</a>

<h3 class="abs gallery-title">............... Our Products Gallery ...............</h3>
<div class="abs thumb" style="left:158px;background:linear-gradient(135deg,#d9c08a,#8a6a48)" role="img" aria-label="Gallery photo: couple with a small dog"></div>
<div class="abs thumb" style="left:260px;background:linear-gradient(135deg,#c9c5bd,#2e2a2a)" role="img" aria-label="Gallery photo: legs in dark leggings"></div>
<div class="abs thumb" style="left:361px;background:linear-gradient(135deg,#2a4d66,#18303f)" role="img" aria-label="Gallery photo: back of a navy jacket"></div>
<div class="abs thumb" style="left:463px;background:linear-gradient(180deg,#dfe6ea,#8fa3ad 60%,#b9b3a6)" role="img" aria-label="Gallery photo: man by the water"></div>
<div class="abs thumb" style="left:565px;background:linear-gradient(135deg,#6f9a4a,#3c5a2a)" role="img" aria-label="Gallery photo: woman in a green park"></div>
<div class="abs thumb" style="left:666px;background:linear-gradient(135deg,#7b8a5a,#3f4636)" role="img" aria-label="Gallery photo: woman cycling on a path"></div>
<div class="abs thumb" style="left:768px;background:linear-gradient(135deg,#e6d2c0,#8c6b58)" role="img" aria-label="Gallery photo: smiling man portrait"></div>
<div class="abs thumb-label" style="left:155px">Lorem Ipsum</div>
<div class="abs thumb-label" style="left:260px">Lorem Ipsum</div>
<div class="abs thumb-label" style="left:353px">Lorem Ipsum</div>
<div class="abs thumb-label" style="left:460px">Lorem Ipsum</div>
<div class="abs thumb-label" style="left:564px">Lorem Ipsum</div>
<div class="abs thumb-label" style="left:665px">Lorem Ipsum</div>
<div class="abs thumb-label" style="left:767px">Lorem Ipsum</div>

<div class="abs base-bar"></div>
<div class="abs base-dot"></div>
<p class="abs copyright">All right reserved with copyright © 2013 www.tandlo-example.com - Terms</p>
<div class="abs base-brand">Tandlo</div>

</body>
</html>
```